Investment website design - investing in mutual funds

I need a design of a website (only homepage for now) dedicated to investment in mutual funds. Attached is a mock up with all the elements the homepage design should contain. The homepage should contain a logo in the upper left corner, the domain the website will run on is www.morvatelsko.cz , in the upper right corner there should be 2 buttons or links SIGN UP / SIGN IN. The bottom of the homepage should contain links to ABOUT US, FAQ, PRIVACY POLICY, CONTACT US.
Now the main elements on the homepage
1) Video that will explain how the investment works exactly, under this video we will have 3 illustrated icons like the ones attached (see 2nd attachement) that will show the potential investor what exactly they could get when investing with us (education for kids, happy life after they retire, regular monthly payment for the rest of their life).
2) On the right side next to the video we will have a calculator where a potential investor can play with the numbers, the investor can fill in the MONTHLY PAYMENT that he wants to invest regularly every month, the time frame of the investment - for how long he wants to invest. Once the potential investor selects those 2 variables we will calculate for him 2 options - either he can get a ONE TIME PAYOUT once he reaches his investment horizon or he can get a regular monthly payment for the rest of his life. Under the laculator there will be a button 'I want to invest ->'. The functionality of the calculator should be similar to the calculator that can be found here http://www.brovikbanka.cz/brovik-podilove-fondy/ and https://pelvaro.cz/.
The design should look similar to https://pelvaro.cz/ (font, colors, logo). We prefer white background in the area where we have the video and calculator. We also like the design of www.truvanex.com. Let me know if you have any questions.

```html
<!DOCTYPE html>
<html lang="en">
<head>
<meta charset="utf-8">
<title>morvatelsko.cz – Mutual Fund Investing</title>
<link rel="stylesheet" href="https://fonts.googleapis.com/css2?family=Roboto:ital,wght@0,300;0,400;0,500;0,700;1,400&family=Amatic+SC:wght@700&family=Montserrat:wght@700&display=swap">
<style>
:root{
  --orange:#e8573a;
  --orange-dark:#c9452c;
  --teal:#1f8a9e;
  --amber:#f3b34a;
  --petrol:#2a8a96;
  --text:#444;
  --muted:#777;
  --light:#f1f1f1;
  --rule:#e2e2e2;
  --white:#fff;
}
*{box-sizing:border-box;margin:0;padding:0}
html,body{width:1200px;height:3965px;overflow:hidden}
body{position:relative;font-family:"Roboto",Arial,sans-serif;color:var(--text);background:var(--white)}
.abs{position:absolute}

/* hero */
.hero{left:0;top:0;width:1200px;height:666px;background:linear-gradient(180deg,#e9907a 0%,#dc6e56 45%,#c24a35 100%)}
.logo{left:48px;top:57px;display:flex;align-items:center;gap:12px;color:var(--white);font-size:36px;font-weight:500}
.logo-dot{width:44px;height:44px;border-radius:50%;background:var(--white)}
.nav{top:64px;right:80px;display:flex;align-items:center;gap:22px;font-size:15px;font-weight:700;color:var(--white);text-transform:uppercase}
.nav .sign-in{background:var(--orange-dark);padding:8px 10px;border:1px solid rgba(255,255,255,.4)}
.video{left:48px;top:243px;width:562px;height:315px;background:#2b2b2b;padding:6px}
.video-screen{width:100%;height:263px;background:linear-gradient(135deg,#f6ddd2,#efc4b0)}
.video-bar{height:34px;display:flex;align-items:center;gap:14px;padding:0 12px;color:#ccc;font-size:11px}
.video-bar .track{flex:1;height:4px;background:#666;position:relative}
.video-bar .track span{position:absolute;left:0;top:0;width:55%;height:4px;background:#ddd}
.calc-title{left:671px;top:180px;width:457px;text-align:center;color:var(--white);font-size:36px;font-weight:400}
.field{left:671px;width:457px;height:52px;background:rgba(255,255,255,.18);border:1px solid rgba(255,255,255,.3);color:var(--white);font-size:17px;padding:14px 20px}
.calc-label{left:671px;color:var(--white);font-size:17px}
.slider{left:671px;top:360px;width:457px;height:2px;background:rgba(255,255,255,.6)}
.slider-knob{left:724px;top:348px;width:26px;height:26px;border-radius:50%;background:var(--white)}
.slider-min,.slider-max{top:366px;color:var(--white);font-size:14px}
.or{left:671px;top:468px;width:457px;text-align:center;color:var(--white);font-size:16px}
.btn-invest{left:938px;top:566px;width:190px;height:52px;background:var(--orange-dark);color:var(--white);font-size:17px;display:flex;align-items:center;justify-content:center;gap:12px}

/* benefits */
.art{border-radius:50%}
.benefit-title{color:var(--teal);font-size:36px;font-weight:400}
.benefit-text{font-size:17px;line-height:23px;color:var(--text)}
.benefit-text em{font-style:normal;color:var(--orange)}

/* borrow */
.borrow-zone{left:0;top:1800px;width:1200px;height:1560px;background:linear-gradient(180deg,#fff 0%,var(--light) 6%,var(--light) 100%)}
.btn-borrow{left:489px;top:1887px;width:219px;height:85px;background:var(--orange);color:var(--white);font-family:"Amatic SC",cursive;font-size:34px;display:flex;align-items:center;justify-content:center;box-shadow:0 4px 10px rgba(0,0,0,.2)}
.hand-title{left:0;width:1200px;text-align:center;color:var(--teal);font-family:"Amatic SC",cursive;font-size:42px}
.item-art{width:118px;height:100px;border-radius:50%}
.loans{left:233px;width:877px}
.loan-row{position:absolute;left:0;width:877px;border-bottom:1px solid var(--rule);font-size:15px}
.loan-row .ic{position:absolute;left:6px;width:80px;height:66px;border-radius:50%;background:radial-gradient(ellipse at center,var(--amber) 0%,rgba(243,179,74,.55) 45%,rgba(243,179,74,0) 72%)}
.loan-row .date{position:absolute;left:132px;color:var(--muted)}
.loan-row .type{position:absolute;left:256px;color:var(--orange);text-decoration:underline}
.loan-row .amount{position:absolute;left:441px;width:270px;line-height:60px;color:var(--text)}
.loan-row .amount b{color:#222}

/* testimonials */
.tag{left:497px;top:3190px;width:145px;height:37px;background:var(--orange);color:var(--white);font-size:14px;display:flex;align-items:center;justify-content:center}
.customers{left:0;top:3246px;width:1200px;text-align:center;font-family:"Montserrat",sans-serif;font-size:32px;color:#222;letter-spacing:2px}
.customers span{color:var(--teal)}
.customers-rule{left:528px;top:3315px;width:146px;height:2px;background:var(--orange)}
.quote-band{left:0;top:3362px;width:1200px;height:312px;background:var(--orange)}
.avatar{left:98px;top:3425px;width:106px;height:106px;border-radius:50%;background:#d9a48c;border:4px solid var(--white)}
.author{left:238px;top:3410px;width:846px;text-align:center;color:var(--white);font-size:16px}
.author b{font-weight:700}
.quote-rule{left:238px;top:3466px;width:846px;height:1px;background:rgba(255,255,255,.5)}
.quote{left:238px;top:3502px;width:846px;text-align:center;color:var(--white);font-style:italic;font-size:16px;line-height:35px}
.pager{left:560px;top:3610px;width:80px;text-align:center;color:var(--white);font-size:26px}
.to-top{left:1018px;top:3669px;width:53px;height:53px;background:var(--orange);display:flex;align-items:center;justify-content:center}

/* footer */
.foot-head{color:var(--teal);font-size:14px;font-weight:700}
.foot-text{font-size:12px;line-height:18px;color:#333}
.foot-list{list-style:none;font-size:12px;color:#333}
.social{left:164px;top:3866px;display:flex;gap:14px}
.social span{width:18px;height:18px;border-radius:50%;background:#777}
.bottom-bar{left:0;top:3920px;width:1200px;height:45px;background:var(--orange);color:var(--white);font-size:12px;padding:15px 172px}
</style>
</head>
<body>

<header>
  <div class="abs hero" role="img" aria-label="Blurred city skyline photo with warm orange overlay"></div>
  <div class="abs logo"><span class="logo-dot"></span>morvatelsko.cz</div>
  <nav class="abs nav">
    <span>Home</span><span>About us</span><span>Why to invest</span><span>FAQ</span><span>Contacts</span><span>Sign up</span><span class="sign-in">Sign in</span>
  </nav>

  <div class="abs video">
    <div class="video-screen" role="img" aria-label="Video still of a rising growth chart over wooden blocks"></div>
    <div class="video-bar">
      <svg width="12" height="14"><rect x="0" y="0" width="4" height="14" fill="#ddd"/><rect x="8" y="0" width="4" height="14" fill="#ddd"/></svg>
      <div class="track"><span></span></div>
      <span>01:46 / 03:20</span>
      <svg width="16" height="14"><path d="M0 4h4l5-4v14l-5-4H0z" fill="#ddd"/></svg>
      <div class="track" style="flex:0 0 60px"><span style="width:60%"></span></div>
      <span>HD</span>
      <svg width="14" height="14" fill="none" stroke="#ddd" stroke-width="2"><path d="M1 5V1h4M9 1h4v4M13 9v4H9M5 13H1V9"/></svg>
    </div>
  </div>

  <h2 class="abs calc-title">Our Online Calculator</h2>
  <div class="abs field" style="top:246px">Regular monthly Investment</div>
  <div class="abs calc-label" style="top:308px">Length Of Investments</div>
  <div class="abs slider"></div>
  <div class="abs slider-knob"></div>
  <div class="abs slider-min" style="left:671px">0</div>
  <div class="abs slider-max" style="left:1068px">30 years</div>
  <div class="abs field" style="top:404px">One time payout</div>
  <div class="abs or">OR</div>
  <div class="abs field" style="top:492px">Monthly payout</div>
  <div class="abs btn-invest">I want to Invest
    <svg width="10" height="14" fill="none" stroke="#fff" stroke-width="2.5"><path d="M2 1l6 6-6 6"/></svg>
  </div>
</header>

<main>
  <section>
    <div class="abs art" style="left:109px;top:700px;width:258px;height:198px;background:radial-gradient(ellipse at center,#f0a13a 0%,rgba(58,166,181,.55) 45%,rgba(58,166,181,0) 72%)" role="img" aria-label="Illustration of a graduation cap on a stack of books"></div>
    <h3 class="abs benefit-title" style="left:462px;top:736px">Education for kids</h3>
    <p class="abs benefit-text" style="left:462px;top:790px;width:714px">Lorem ipsum dolor sit amet, error regione eum et. Vim essent cetero mnesarchum in, mei erat necessitatibus ut. No quo <em>expetenda</em> abhorreant repudiandae, veritus suscipit inimicus cu pri, mei aliquam facilisis ut. Id eum iriure diceret omnesque, latine tamquam philosophia per eu.</p>

    <h3 class="abs benefit-title" style="left:111px;top:960px">Passive Income</h3>
    <p class="abs benefit-text" style="left:111px;top:1014px;width:640px">Lorem ipsum dolor sit amet, error regione eum et. Vim essent cetero mnesarchum in, mei erat necessitatibus ut. No quo expetenda abhorreant repudiandae, veritus suscipit inimicus cu pri, <em>mei aliquam facilisis ut.</em> Id eum iriure diceret omnesque, latine tamquam philosophia per eu.</p>
    <div class="abs art" style="left:783px;top:860px;width:311px;height:290px;background:radial-gradient(ellipse at center,#e8573a 0%,rgba(243,179,74,.55) 45%,rgba(243,179,74,0) 72%)" role="img" aria-label="Illustration of a cuckoo clock with falling coins"></div>

    <div class="abs art" style="left:175px;top:1229px;width:271px;height:291px;background:radial-gradient(ellipse at center,#e8573a 0%,rgba(42,138,150,.55) 45%,rgba(42,138,150,0) 72%)" role="img" aria-label="Illustration of a retired man playing golf"></div>
    <h3 class="abs benefit-title" style="left:478px;top:1238px">Happy Retirement</h3>
    <p class="abs benefit-text" style="left:478px;top:1292px;width:698px">Lorem ipsum dolor sit amet, error regione eum et. Vim essent cetero mnesarchum in, mei erat necessitatibus ut. No quo <em>expetenda</em> abhorreant repudiandae, veritus suscipit inimicus cu pri, mei aliquam facilisis ut. Id eum iriure diceret omnesque, latine tamquam philosophia per eu.</p>

    <h3 class="abs benefit-title" style="left:111px;top:1576px">Relax and Enjoy</h3>
    <p class="abs benefit-text" style="left:111px;top:1630px;width:640px">Lorem ipsum dolor sit amet, error regione eum et. Vim essent cetero mnesarchum in, mei erat necessitatibus ut. No quo expetenda abhorreant repudiandae, <em>veritus suscipit inimicus cu pri</em>, mei aliquam facilisis ut. Id eum iriure diceret omnesque, latine tamquam philosophia per eu.</p>
    <div class="abs art" style="left:770px;top:1533px;width:324px;height:225px;background:radial-gradient(ellipse at center,#f3b34a 0%,rgba(42,138,150,.5) 45%,rgba(42,138,150,0) 72%)" role="img" aria-label="Illustration of a man sleeping on a beanbag"></div>
  </section>

  <section>
    <div class="abs borrow-zone"></div>
    <svg class="abs" style="left:0;top:1990px" width="1200" height="560"><polygon points="0,40 1200,0 1200,520 0,560" fill="#fff"/></svg>
    <div class="abs btn-borrow">I want to borrow</div>
    <h3 class="abs hand-title" style="top:2068px">What I can borrow</h3>

    <div class="abs item-art" style="left:205px;top:2150px;background:radial-gradient(ellipse at center,var(--amber) 0%,rgba(243,179,74,.5) 42%,rgba(243,179,74,0) 70%)" role="img" aria-label="Icon of banknotes being refinanced"></div>
    <div class="abs item-art" style="left:364px;top:2150px;background:radial-gradient(ellipse at center,var(--petrol) 0%,rgba(42,138,150,.5) 42%,rgba(42,138,150,0) 70%)" role="img" aria-label="Icon of a car"></div>
    <div class="abs item-art" style="left:536px;top:2150px;background:radial-gradient(ellipse at center,var(--orange) 0%,rgba(232,87,58,.5) 42%,rgba(232,87,58,0) 70%)" role="img" aria-label="Icon of household furniture"></div>
    <div class="abs item-art" style="left:713px;top:2150px;background:radial-gradient(ellipse at center,var(--orange) 0%,rgba(243,179,74,.5) 42%,rgba(243,179,74,0) 70%)" role="img" aria-label="Icon of a moving van"></div>
    <div class="abs item-art" style="left:879px;top:2150px;background:radial-gradient(ellipse at center,var(--petrol) 0%,rgba(232,87,58,.45) 42%,rgba(232,87,58,0) 70%)" role="img" aria-label="Icon of a jumping person"></div>
    <div class="abs item-art" style="left:293px;top:2327px;background:radial-gradient(ellipse at center,var(--orange) 0%,rgba(232,87,58,.5) 42%,rgba(232,87,58,0) 70%)" role="img" aria-label="Icon of a toolbox"></div>
    <div class="abs item-art" style="left:451px;top:2327px;background:radial-gradient(ellipse at center,#555 0%,rgba(85,85,85,.45) 42%,rgba(85,85,85,0) 70%)" role="img" aria-label="Icon of a computer and electronics"></div>
    <div class="abs item-art" style="left:628px;top:2327px;background:radial-gradient(ellipse at center,var(--amber) 0%,rgba(243,179,74,.5) 42%,rgba(243,179,74,0) 70%)" role="img" aria-label="Icon of an airplane for travel"></div>
    <div class="abs item-art" style="left:792px;top:2327px;background:radial-gradient(ellipse at center,var(--amber) 0%,rgba(243,179,74,.5) 42%,rgba(243,179,74,0) 70%)" role="img" aria-label="Icon of a mystery box"></div>

    <h3 class="abs hand-title" style="top:2578px">People are just borrowing on ...</h3>
    <div class="abs loans" style="top:2635px">
      <div class="loan-row" style="top:0;height:92px"><div class="ic" style="top:12px" role="img" aria-label="Refinancing icon"></div><span class="date" style="top:36px">11. 11. at 03:57</span><span class="type" style="top:36px">Refinancing</span><span class="amount" style="top:15px"><b>170 000 CZK</b> on 5 years</span></div>
      <div class="loan-row" style="top:92px;height:92px"><div class="ic" style="top:12px" role="img" aria-label="Refinancing icon"></div><span class="date" style="top:36px">11. 11. at 03:50</span><span class="type" style="top:36px">Refinancing</span><span class="amount" style="top:15px"><b>310 000 CZK</b> on 7 years</span></div>
      <div class="loan-row" style="top:184px;height:140px"><div class="ic" style="top:12px" role="img" aria-label="Refinancing icon"></div><span class="date" style="top:36px">11. 11. at 01:33</span><span class="type" style="top:36px">Refinancing</span><span class="amount" style="top:15px"><b>230 000 CZK</b> on 5 years and 6 months</span></div>
      <div class="loan-row" style="top:324px;height:164px"><div class="ic" style="top:34px;background:radial-gradient(ellipse at center,var(--orange) 0%,rgba(232,87,58,.5) 45%,rgba(232,87,58,0) 72%)" role="img" aria-label="Household icon"></div><span class="date" style="top:58px">11. 11. at 01:15</span><span class="type" style="top:58px">Household</span><span class="amount" style="top:37px"><b>50 000 CZK</b> on 3 years and 1 month</span></div>
    </div>
  </section>

  <section>
    <div class="abs tag">TESTIMONIALS</div>
    <h3 class="abs customers"><span>CUSTOMERS</span> SAY'S</h3>
    <div class="abs customers-rule"></div>
    <div class="abs quote-band"></div>
    <div class="abs avatar" role="img" aria-label="Customer portrait photo"></div>
    <p class="abs author"><b>LENA MARSH</b> - UNITED KINGDOM</p>
    <div class="abs quote-rule"></div>
    <p class="abs quote">Lorem ipsum dolor sit amet, error regione eum et. Vim essent cetero mnesarchum in, mei erat necessitatibus ut. No quo expetenda abhorreant repudiandae, veritus suscipit inimicus cu pri, mei aliquam facilisis ut. Id eum iriure diceret omnesque, latine tamquam philosophia per eu.</p>
    <div class="abs pager">‹ ›</div>
    <div class="abs to-top"><svg width="18" height="12" fill="none" stroke="#fff" stroke-width="2.5"><path d="M1 11l8-8 8 8"/></svg></div>
  </section>
</main>

<footer>
  <h4 class="abs foot-head" style="left:164px;top:3720px">About Us</h4>
  <p class="abs foot-text" style="left:164px;top:3746px;width:330px">Lorem ipsum dolor sit amet adipiscing elit sed ullamco laboris nisi in voluptate explicabo fugiat nulla pariatur.</p>
  <h4 class="abs foot-head" style="left:164px;top:3834px">Get Socialize us with</h4>
  <div class="abs social"><span></span><span></span><span></span><span></span></div>

  <h4 class="abs foot-head" style="left:595px;top:3720px">Quick Links</h4>
  <ul class="abs foot-list" style="left:595px;top:3748px;line-height:25px">
    <li>Home</li><li>Availability</li><li>About Us</li><li>FAQs</li>
  </ul>

  <h4 class="abs foot-head" style="left:835px;top:3720px">Terms &amp; Conditions</h4>
  <ul class="abs foot-list" style="left:835px;top:3750px;line-height:31px">
    <li>Privacy &amp; Policy</li><li>Testimonials</li><li>Get in Touch</li>
  </ul>

  <div class="abs bottom-bar">© 2016 morvatelsko.cz All rights reserved.</div>
</footer>

</body>
</html>
```